business cards, stationary, email signature
Professional
Greta Volsky
President
Corporate office:
3620 E Tamsin Road, Orange, CA 92814
Other locations in San Diego, CA and Reno, NV
greta@farwellgrp.net
www.farwellgrp.net
482650, K, D74
*8(a), *SDB, *SBE, *MBE, *DBE, *CBE
these certifications should be listed in the middle, bottom of the card.
■221119 – Other Electric Power Generation
■236210 – Industrial Building Construction
■236220 – Commercial and Institutional Building Construction
■237310 – Highway, Street, and Bridge Construction
■238160 – Roofing Contractors
■238170 – Siding Contractors
■238220 – Plumbing, Heating, and Air-Conditioning Contractors
■238310 – Drywall and Insulation Contractors
■238320 – Painting and Wall Covering Contractors
■238340 – Tile and Terrazzo Contractors
■238350 – Finish Carpentry Contractors
■238390 – Other Building Finishing Contractors
■238910 – Site Preparation Contractors
■238990 – All Other Specialty Trade Contractors
■541350 – Building Inspection Services
■561210 – Facilities Support Services
■561790 – Other Services to Buildings and Dwellings

```html
<!DOCTYPE html>
<html lang="en">
<head>
<meta charset="utf-8">
<title>Farwell Group – Business Cards</title>
<link href="https://fonts.googleapis.com/css2?family=Cinzel:wght@400&family=Open+Sans:wght@400;600;700&display=swap" rel="stylesheet">
<style>
  :root {
    --page-bg: #e9e6e1;
    --card-top: #3a3a3c;
    --card-mid: #1c1c1e;
    --card-bottom: #0b0b0c;
    --swoosh: #8a8a8e;
    --swoosh-light: #c9c9cd;
    --text-main: #f2f2f2;
    --text-soft: #bfc3c7;
    --brand-blue: #7ab8e4;
    --brand-sun: #f0b52c;
  }
  * { margin: 0; padding: 0; box-sizing: border-box; }
  html, body { width: 1200px; height: 665px; overflow: hidden; }
  body {
    background: var(--page-bg);
    font-family: "Open Sans", Arial, sans-serif;
    position: relative;
  }
  .card {
    position: absolute;
    top: 182px;
    width: 520px;
    height: 300px;
    border-radius: 22px;
    overflow: hidden;
    background: linear-gradient(160deg, var(--card-top) 0%, var(--card-mid) 45%, var(--card-bottom) 100%);
    box-shadow: 0 8px 22px rgba(0,0,0,0.35);
    color: var(--text-main);
  }
  .card--front { left: 60px; }
  .card--back { left: 620px; }
  .card__swoosh { position: absolute; inset: 0; width: 100%; height: 100%; }

  .brand { position: absolute; left: 34px; top: 30px; display: flex; align-items: center; gap: 18px; }
  .brand__mark { width: 78px; height: 78px; border-radius: 50%; background: var(--brand-sun); }
  .brand__name {
    font-family: "Cinzel", Georgia, serif;
    font-size: 38px;
    letter-spacing: 2px;
    color: var(--brand-blue);
  }
  .license {
    position: absolute; right: 34px; top: 118px;
    font-size: 10px; line-height: 14px; color: var(--text-soft);
  }
  .contact {
    position: absolute; left: 0; right: 0; top: 160px;
    text-align: center; font-size: 10px; line-height: 15px; color: var(--text-soft);
  }
  .contact__person { font-size: 13px; font-weight: 700; color: var(--text-main); margin-bottom: 4px; }
  .contact__person span { font-weight: 400; color: var(--text-soft); }
  .contact__row span + span { margin-left: 14px; }
  .certifications { margin-top: 2px; color: var(--text-main); }

  .naics {
    position: absolute; left: 30px; top: 20px;
    list-style: none; font-size: 10.5px; line-height: 15.4px; color: var(--text-main);
  }
  .naics li::before { content: "■"; margin-right: 2px; font-size: 9px; }
  .back-brand {
    position: absolute; right: 26px; bottom: 16px;
    display: flex; align-items: center; gap: 8px;
  }
  .back-brand__mark { width: 40px; height: 40px; border-radius: 50%; background: var(--brand-sun); }
  .back-brand__name { font-family: "Cinzel", Georgia, serif; font-size: 13px; color: var(--brand-blue); }
</style>
</head>
<body>

  <section class="card card--front" aria-label="Business card front">
    <svg class="card__swoosh" viewBox="0 0 520 300" preserveAspectRatio="none" aria-hidden="true">
      <path d="M0 172 C150 142 360 138 520 150 L520 300 L0 300 Z" fill="#101012"/>
      <path d="M0 172 C150 142 360 138 520 150" fill="none" stroke="var(--swoosh-light)" stroke-width="3"/>
      <path d="M0 179 C150 150 360 146 520 157" fill="none" stroke="var(--swoosh)" stroke-width="1.5" opacity="0.6"/>
    </svg>
    <div class="brand">
      <div class="brand__mark"></div>
      <div class="brand__name">FARWELL GROUP</div>
    </div>
    <div class="license">License # 482650, K, D74</div>
    <div class="contact">
      <div class="contact__person">Greta Volsky <span>· President</span></div>
      <div class="contact__row"><span>TF: 1.888.406.5530</span><span>P: 1.714.402.7731</span><span>C: 1.714.309.6684</span></div>
      <div class="contact__row"><span>F: 1.714.402.7731</span><span>E: greta@farwellgrp.net</span><span>W: www.farwellgrp.net</span></div>
      <div class="contact__row">Corporate office: 3620 E Tamsin Road, Orange, CA 92814</div>
      <div class="contact__row">Other locations in San Diego, CA and Reno, NV</div>
      <div class="certifications">Certifications: *8(a), *SDB, *SBE, *MBE, *DBE, *CBE</div>
    </div>
  </section>

  <section class="card card--back" aria-label="Business card back">
    <svg class="card__swoosh" viewBox="0 0 520 300" preserveAspectRatio="none" aria-hidden="true">
      <path d="M320 300 C340 220 430 180 520 165 L520 300 Z" fill="#121214"/>
      <path d="M320 300 C340 220 430 180 520 165" fill="none" stroke="var(--swoosh)" stroke-width="2.5"/>
    </svg>
    <ul class="naics">
      <li>221119 – Other Electric Power Generation</li>
      <li>236210 – Industrial Building Construction</li>
      <li>236220 – Commercial and Institutional Building Construction</li>
      <li>237310 – Highway, Street, and Bridge Construction</li>
      <li>238160 – Roofing Contractors</li>
      <li>238170 – Siding Contractors</li>
      <li>238220 – Plumbing, Heating, and Air-Conditioning Contractors</li>
      <li>238310 – Drywall and Insulation Contractors</li>
      <li>238320 – Painting and Wall Covering Contractors</li>
      <li>238340 – Tile and Terrazzo Contractors</li>
      <li>238350 – Finish Carpentry Contractors</li>
      <li>238390 – Other Building Finishing Contractors</li>
      <li>238910 – Site Preparation Contractors</li>
      <li>238990 – All Other Specialty Trade Contractors</li>
      <li>541350 – Building Inspection Services</li>
      <li>561210 – Facilities Support Services</li>
      <li>561790 – Other Services to Buildings and Dwellings</li>
    </ul>
    <div class="back-brand">
      <div class="back-brand__mark"></div>
      <div class="back-brand__name">FARWELL GROUP</div>
    </div>
  </section>

</body>
</html>
```